Irrigation Business needs their business cards modernised and revamped

I would like to keep my current logo, colours and revamp the format of the card.

I would like the card to be clean yet important.

Im not sure if you include texture but i would like the named logo to be indented into the card etc.

show me something alive and free something thats clinical to the point yet has a feel of achievement. i would like people to go nice card.

Target Market(s)

high end clients, corporate, sports field manger, the guys that make the decisions

Industry/Entity Type

Business

Contact Information for Business Card

nformation to be included

Dorian Hesk (Director)
0487253916
dorian@tfcraft.biz
www.taddsfieldcrafts.com

instagram logo
google logo
facebook logo

Colors

Designer to choose colors to be used in the design.

Requirements
Nice to have
• indentations a really nice feel to the card good texture

```html
<!DOCTYPE html>
<html lang="en">
<head>
<meta charset="utf-8">
<title>Tadds Field Crafts — Business Card</title>
<link href="https://fonts.googleapis.com/css2?family=Roboto:wght@400;500;700;900&display=swap" rel="stylesheet">
<style>
  :root {
    --backdrop: #2a2a2c;
    --card: #1e1f22;
    --brand-blue: #3a63ad;
    --sky-blue: #3ea2dc;
    --deep-blue: #33579a;
    --field-green: #1d9a50;
    --emboss: #3a3b40;
    --emboss-light: #55575e;
    --white: #ffffff;
    --muted: #d9dbe0;
  }
  * { box-sizing: border-box; margin: 0; padding: 0; }
  html, body {
    width: 799px; height: 1200px; overflow: hidden;
    background: var(--backdrop);
    font-family: "Roboto", Arial, sans-serif;
  }
  .sheet { position: relative; width: 799px; height: 1200px; }
  .card {
    position: absolute; left: 100px; width: 600px; height: 343px;
    background: var(--card);
    border-radius: 3px;
    box-shadow: 0 14px 30px rgba(0,0,0,.45);
    overflow: hidden;
  }
  .card--front { top: 120px; }
  .card--back { top: 730px; }

  /* Front */
  .front-mark {
    position: absolute; left: 220px; top: 58px;
    width: 160px; height: 160px; border-radius: 50%;
    background: radial-gradient(circle at 35% 30%, var(--emboss-light), var(--emboss) 60%, #2c2d31);
    box-shadow: inset 2px 3px 5px rgba(0,0,0,.6), inset -1px -1px 2px rgba(255,255,255,.08);
    display: flex; align-items: center; justify-content: center;
    text-align: center;
  }
  .front-mark__name {
    font-weight: 900; font-size: 17px; line-height: 1.2;
    letter-spacing: 1px; color: #1b1c1f;
    text-transform: uppercase;
  }
  .front-rule {
    position: absolute; top: 262px; height: 2px;
    background: linear-gradient(90deg, transparent, var(--brand-blue));
  }
  .front-rule--left { left: 110px; width: 140px; }
  .front-rule--right { left: 350px; width: 140px; background: linear-gradient(90deg, var(--brand-blue), transparent); }
  .social { display: flex; gap: 8px; }
  .social__dot { width: 20px; height: 20px; border-radius: 50%; background: var(--brand-blue); }
  .social__dot:nth-child(2) { background: var(--sky-blue); }
  .social__dot:nth-child(3) { background: var(--deep-blue); }
  .front-social { position: absolute; left: 266px; top: 253px; }

  /* Back */
  .back-band {
    position: absolute; left: 0; right: 0; top: 222px; bottom: 0;
    background: linear-gradient(180deg, var(--sky-blue) 0%, var(--deep-blue) 40%, var(--deep-blue) 100%);
  }
  .brand {
    position: absolute; left: 36px; top: 30px;
    display: flex; flex-direction: column; align-items: center; width: 250px;
  }
  .brand__disc {
    width: 96px; height: 96px; border-radius: 50%;
    background: var(--sky-blue);
    margin-bottom: 12px;
  }
  .brand__name {
    font-weight: 900; font-size: 24px; letter-spacing: .5px;
    color: var(--brand-blue); text-transform: uppercase; text-align: center; line-height: 1.1;
  }
  .person { position: absolute; right: 36px; top: 100px; text-align: right; }
  .person__name {
    font-weight: 900; font-size: 22px; color: var(--sky-blue);
    text-transform: uppercase; letter-spacing: .3px;
  }
  .person__role { font-size: 12px; color: var(--muted); margin-top: 2px; }
  .person .social { justify-content: flex-end; margin-top: 10px; }
  .contact {
    position: absolute; right: 36px; bottom: 22px;
    list-style: none; text-align: right;
  }
  .contact__item {
    display: flex; align-items: center; justify-content: flex-end; gap: 8px;
    color: var(--white); font-size: 15px; line-height: 22px;
  }
  .contact__icon { width: 14px; height: 14px; fill: none; stroke: var(--white); stroke-width: 1.6; }
</style>
</head>
<body>
<main class="sheet">

  <section class="card card--front" aria-label="Card front">
    <div class="front-mark">
      <span class="front-mark__name">Tadds<br>Field<br>Crafts</span>
    </div>
    <span class="front-rule front-rule--left"></span>
    <div class="social front-social" aria-label="Social profiles">
      <span class="social__dot"></span><span class="social__dot"></span><span class="social__dot"></span>
    </div>
    <span class="front-rule front-rule--right"></span>
  </section>

  <section class="card card--back" aria-label="Card back">
    <div class="back-band" role="img" aria-label="Flowing green and blue wave bands across the lower card"></div>

    <div class="brand">
      <span class="brand__disc"></span>
      <span class="brand__name">Tadds Field Crafts</span>
    </div>

    <div class="person">
      <p class="person__name">Dorian Hesk</p>
      <p class="person__role">Director</p>
      <div class="social" aria-label="Social profiles">
        <span class="social__dot"></span><span class="social__dot"></span><span class="social__dot"></span>
      </div>
    </div>

    <ul class="contact">
      <li class="contact__item">0487253916
        <svg class="contact__icon" viewBox="0 0 16 16"><path d="M3 2h3l1.5 3.5-2 1.2a8 8 0 0 0 3.8 3.8l1.2-2L14 10v3a1 1 0 0 1-1 1A11 11 0 0 1 2 3a1 1 0 0 1 1-1z"/></svg>
      </li>
      <li class="contact__item">dorian@tfcraft.biz
        <svg class="contact__icon" viewBox="0 0 16 16"><rect x="1.5" y="3.5" width="13" height="9"/><path d="M1.5 3.5 8 9l6.5-5.5"/></svg>
      </li>
      <li class="contact__item">taddsfieldcrafts.com
        <svg class="contact__icon" viewBox="0 0 16 16"><circle cx="8" cy="8" r="6.5"/><path d="M1.5 8h13M8 1.5c-3 3.5-3 9.5 0 13M8 1.5c3 3.5 3 9.5 0 13"/></svg>
      </li>
    </ul>
  </section>

</main>
</body>
</html>
```